Garage Door Business Truck Wrap

looking to create a wrap for a 2012 brannock velmaro 2500 HD single cab with service bed. please use creativity, here is the website www.halvordgaragedoorservices.com.. Also, I will upload documents of branded items, Id like everything to seamlessly flow together

```html
<!DOCTYPE html>
<html lang="en">
<head>
<meta charset="utf-8">
<title>Halvord Garage – Service Truck Wrap Concepts</title>
<link rel="stylesheet" href="https://fonts.googleapis.com/css2?family=Oswald:wght@500;600&family=Poppins:wght@500;600&display=swap">
<style>
  :root {
    --canvas: #ffffff;
    --wrap-black: #0d0d0d;
    --wrap-gold: #a8852c;
    --wrap-gold-light: #c9a545;
    --wrap-gold-dark: #6f5518;
    --glass: #3a3f44;
    --trim: #bfc3c7;
    --text-light: #f4f1ea;
    --text-gold: #d8b457;
    --text-dark: #1a1408;
  }
  * { margin: 0; padding: 0; box-sizing: border-box; }
  html, body { width: 1200px; height: 1200px; overflow: hidden; background: var(--canvas); }
  .wrap-sheet {
    width: 1200px; height: 1200px;
    display: flex; flex-direction: column; justify-content: space-between;
    padding: 18px 180px;
  }
  .wrap-concept { width: 840px; height: 372px; display: block; }
  .label-sans { font-family: "Oswald", sans-serif; font-weight: 600; }
  .label-round { font-family: "Poppins", sans-serif; font-weight: 600; }
  .brand-name { font-family: "Oswald", sans-serif; font-weight: 500; fill: var(--text-gold); letter-spacing: 3px; }
</style>
</head>
<body>
<main class="wrap-sheet">

  <!-- Concept 1: gold swoosh cab, full gold service bed -->
  <svg class="wrap-concept" viewBox="0 0 840 372" aria-label="Wrap concept one">
    <defs>
      <linearGradient id="gold1" x1="0" y1="0" x2="1" y2="1">
        <stop offset="0" stop-color="var(--wrap-gold-light)"/>
        <stop offset="1" stop-color="var(--wrap-gold-dark)"/>
      </linearGradient>
    </defs>
    <!-- cab body -->
    <path class="cab-panel" d="M20 150 L215 122 L290 48 L420 42 L420 290 L195 290 A68 68 0 0 0 60 290 L20 290 Z" fill="var(--wrap-black)"/>
    <path class="cab-window" d="M300 62 L400 58 L400 150 L240 150 Z" fill="var(--glass)"/>
    <path class="hood-swoosh" d="M20 150 L215 122 L250 88 L270 92 L230 150 C150 158 80 168 20 178 Z" fill="url(#gold1)"/>
    <path class="cab-stripe" d="M140 262 L420 250 L420 272 L130 280 Z" fill="url(#gold1)"/>
    <text class="label-sans" x="48" y="208" font-size="15" fill="var(--text-gold)">LICENSED AND INSURED</text>
    <circle cx="282" cy="200" r="6" fill="var(--text-gold)"/>
    <text class="brand-name" x="282" y="232" font-size="22" text-anchor="middle">HALVORD GARAGE</text>
    <text class="label-round" x="280" y="268" font-size="10.5" text-anchor="middle" fill="var(--text-dark)">www.halvordgaragedoorservices.com</text>
    <!-- service bed -->
    <rect class="bed-rail" x="430" y="118" width="380" height="12" fill="var(--trim)"/>
    <path class="bed-panel" d="M430 130 L810 130 L810 280 L735 280 A68 68 0 0 0 600 280 L430 280 Z" fill="url(#gold1)"/>
    <rect x="470" y="160" width="300" height="70" fill="var(--wrap-gold-dark)" opacity=".35" role="img" aria-label="Faint garage door illustration across the service bed"/>
    <text class="label-round" x="620" y="178" font-size="24" text-anchor="middle" fill="var(--text-dark)">(555) 014-2270</text>
    <circle class="badge-plain" cx="772" cy="240" r="20" fill="var(--text-light)" opacity=".85"/>
  </svg>

  <!-- Concept 2: gold hood cab, banded service bed -->
  <svg class="wrap-concept" viewBox="0 0 840 372" aria-label="Wrap concept two">
    <defs>
      <linearGradient id="gold2" x1="0" y1="0" x2="1" y2="1">
        <stop offset="0" stop-color="var(--wrap-gold-light)"/>
        <stop offset="1" stop-color="var(--wrap-gold-dark)"/>
      </linearGradient>
    </defs>
    <path class="cab-panel" d="M20 150 L215 122 L290 48 L420 42 L420 290 L195 290 A68 68 0 0 0 60 290 L20 290 Z" fill="var(--wrap-black)"/>
    <path class="hood-gold" d="M20 150 L215 122 L290 48 L420 42 L420 118 C300 130 150 150 20 178 Z" fill="url(#gold2)"/>
    <path class="cab-window" d="M300 62 L400 58 L400 150 L240 150 Z" fill="var(--glass)"/>
    <path class="cab-accent" d="M330 290 L420 230 L420 290 Z" fill="url(#gold2)"/>
    <circle cx="282" cy="196" r="6" fill="var(--text-gold)"/>
    <text class="brand-name" x="282" y="230" font-size="22" text-anchor="middle">HALVORD GARAGE</text>
    <rect class="bed-rail" x="430" y="118" width="380" height="12" fill="var(--trim)"/>
    <path class="bed-panel" d="M430 130 L810 130 L810 280 L735 280 A68 68 0 0 0 600 280 L430 280 Z" fill="url(#gold2)"/>
    <rect class="bed-band" x="430" y="130" width="380" height="34" fill="var(--wrap-black)"/>
    <rect class="bed-web-strip" x="430" y="164" width="380" height="20" fill="#2a2112"/>
    <rect x="470" y="196" width="300" height="40" fill="var(--wrap-gold-dark)" opacity=".35" role="img" aria-label="Faint garage door illustration across the service bed"/>
    <text class="label-round" x="442" y="155" font-size="20" fill="var(--text-light)">(555) 014-2270</text>
    <text class="label-sans" x="798" y="154" font-size="15" text-anchor="end" fill="var(--text-gold)">LICENSED AND INSURED</text>
    <text class="label-round" x="640" y="178" font-size="10.5" text-anchor="middle" fill="var(--text-light)">www.halvordgaragedoorservices.com</text>
    <circle class="badge-plain" cx="772" cy="240" r="20" fill="var(--text-light)" opacity=".85"/>
  </svg>

  <!-- Concept 3: all-black cab, banded service bed -->
  <svg class="wrap-concept" viewBox="0 0 840 372" aria-label="Wrap concept three">
    <defs>
      <linearGradient id="gold3" x1="0" y1="0" x2="1" y2="1">
        <stop offset="0" stop-color="var(--wrap-gold-light)"/>
        <stop offset="1" stop-color="var(--wrap-gold-dark)"/>
      </linearGradient>
    </defs>
    <path class="cab-panel" d="M20 150 L215 122 L290 48 L420 42 L420 290 L195 290 A68 68 0 0 0 60 290 L20 290 Z" fill="var(--wrap-black)"/>
    <path class="cab-window" d="M300 62 L400 58 L400 150 L240 150 Z" fill="var(--glass)"/>
    <path class="cab-accent" d="M330 290 L420 230 L420 290 Z" fill="url(#gold3)"/>
    <circle cx="282" cy="196" r="6" fill="var(--text-gold)"/>
    <text class="brand-name" x="282" y="230" font-size="22" text-anchor="middle">HALVORD GARAGE</text>
    <rect class="bed-rail" x="430" y="118" width="380" height="12" fill="var(--trim)"/>
    <path class="bed-panel" d="M430 130 L810 130 L810 280 L735 280 A68 68 0 0 0 600 280 L430 280 Z" fill="url(#gold3)"/>
    <rect class="bed-band" x="430" y="130" width="380" height="34" fill="var(--wrap-black)"/>
    <rect class="bed-web-strip" x="430" y="164" width="380" height="20" fill="#2a2112"/>
    <rect x="470" y="196" width="300" height="40" fill="var(--wrap-gold-dark)" opacity=".35" role="img" aria-label="Faint garage door illustration across the service bed"/>
    <text class="label-round" x="442" y="155" font-size="20" fill="var(--text-light)">(555) 014-2270</text>
    <text class="label-sans" x="798" y="154" font-size="15" text-anchor="end" fill="var(--text-gold)">LICENSED AND INSURED</text>
    <text class="label-round" x="640" y="178" font-size="10.5" text-anchor="middle" fill="var(--text-light)">www.halvordgaragedoorservices.com</text>
    <circle class="badge-plain" cx="772" cy="240" r="20" fill="var(--text-light)" opacity=".85"/>
  </svg>

</main>
</body>
</html>
```